Pactwise - Training I Consulting I Review - Related to Contracts/Agreements

We provide legal services, we need a plattform to book video online trainings or local trainings classes and appointments (with calendar feature to select date and see availability at screen), payment over internet, legal document creation over webpage, videos will be produces in the next 3 - 4 moths so this is a place holder item. Participants for the Online trainings shall have a login in area with secured password. Appointments for local trainings and Consulting. Consider Outline in file attached. I can send you also a video with more explanation regarding the purpose.

Target Market(s)

Startup/scale up Software companies that intent to have an international business and need help with their contracts, to sell their products. Sales persons.

Industry/Entity Type

Legal

Coding

Coded - Design and coding required

Number of Pages Required

5+ page

Font styles to use
Serif
Sans Serif

Colors
000000
eeeeee
f5f5f5
ffffff
f8fcfd
3277b5
ecf7fb
cadf82
86cfc6

Requirements
Must have
• See file pactwise attached with outline. Moreover see here first starting point: https://moritz-ebbing.sitebuildr-demo.net/mysite-1 . Main inspiration comes from www.advisoryhub-demo.net from the log in area, see the outline in the file attached with the screen shots. At the end I need someone who can draft the full webpage and maintain it for a yearly fee. It must be simple and well structured layout. Lean. 1st landing page shall not scroll, 2 landing page only a little to see the testimonials and foster of page. There should be a Progress Bar to indicate the booking/selection process. Calendar booking. Easy fast booking.
• I like the colour mix, the feeling and the easy structor of:
• https://www.artpitch-demo.net/design/6374387or
• https://www.artpitch-demo.net/design/6372391 or https://www.artpitch-demo.net/design/6374366
• https://www.agencyfind-demo.net/en/web-design/belgium-be
• https://www.artpitch-demo.net/design/5896857
• https://www.artpitch-demo.net/design/5902173
• https://www.artpitch-demo.net/design/17197349
• https://www.artpitch-demo.net/design/5464461
• https://www.artpitch-demo.net/design/7180908
Nice to have
• page for evaluation and interview, see outline attached in the file with screen shots. Document upload.
Should not have
• many pictures, long scroll down pages on the 1st and 2nd ladding pages, many colours and forms. No need for news letter, search field, no need for links to Chatterly and other social media (except workNet).

```html
<!DOCTYPE html>
<html lang="en">
<head>
<meta charset="utf-8">
<title>Pactwise</title>
<link rel="stylesheet" href="https://fonts.googleapis.com/css2?family=Open+Sans:wght@400;600;700&family=Oswald:wght@500&display=swap">
<style>
:root{
  --blue-deep:#0a3fa8;
  --blue:#0d52c4;
  --blue-bright:#1565d8;
  --heading-blue:#3a6cc8;
  --link-blue:#1450b8;
  --ink:#1e1e1e;
  --text:#333333;
  --white:#ffffff;
  --mist:#eef2f8;
  --footer:#262626;
  --star:#b5b5b5;
}
*{margin:0;padding:0;box-sizing:border-box}
html,body{width:1005px;height:1200px;overflow:hidden}
body{font-family:"Open Sans",Arial,sans-serif;color:var(--text);background:var(--white);position:relative}
.wrap{position:absolute;left:0;width:1005px}

/* Hero */
.hero{top:0;height:420px;background:linear-gradient(100deg,#0b3fa6 0%,#0c4cc0 45%,#0a47b8 70%,#1257cc 100%);overflow:hidden}
.hero-photo{position:absolute;left:0;top:0;width:1005px;height:420px;
  background:radial-gradient(ellipse 260px 200px at 640px 270px,rgba(60,120,230,.45),transparent 70%),
             radial-gradient(ellipse 300px 260px at 80px 160px,rgba(40,100,210,.4),transparent 70%),
             linear-gradient(180deg,rgba(10,40,130,.2),rgba(20,80,200,.15))}
.logo{position:absolute;font-family:"Open Sans",Arial,sans-serif;font-weight:400;color:var(--white);letter-spacing:1px}
.hero .logo{left:210px;top:12px;font-size:22px}
.nav{position:absolute;top:21px;left:501px;display:flex;align-items:center}
.nav a{color:var(--white);text-decoration:none;font-size:9.5px;font-weight:700;letter-spacing:.4px;margin-right:19px}
.nav .login{margin-left:-1px;margin-right:0;background:var(--white);color:var(--link-blue);width:84px;height:25px;display:flex;align-items:center;justify-content:center;font-size:10px;border-radius:2px;letter-spacing:.8px}
.hero h1{position:absolute;left:209px;top:155px;font-size:37px;font-weight:700;color:var(--white);letter-spacing:.5px}
.hero p{position:absolute;left:209px;top:201px;width:310px;font-size:14px;line-height:21.5px;color:#e8eefc}
.enter{position:absolute;left:209px;top:277px;width:90px;height:30px;background:var(--white);color:var(--link-blue);font-size:10px;font-weight:700;letter-spacing:1px;display:flex;align-items:center;justify-content:center;border-radius:2px;text-decoration:none}

/* Services */
.services{top:420px;height:330px;background:var(--white)}
.section-title{position:absolute;left:0;width:1005px;text-align:center;font-size:25px;font-weight:400;letter-spacing:.8px}
.services .section-title{top:38px;color:var(--heading-blue)}
.service{position:absolute;top:82px;width:180px;height:200px;text-align:center}
.service .brush{position:absolute;left:-4px;top:0;width:188px;height:190px;background:radial-gradient(ellipse at center,var(--mist) 55%,rgba(238,242,248,0) 75%)}
.service .icon{position:relative;display:block;margin:24px auto 0;width:56px;height:56px;border-radius:6px;background:linear-gradient(135deg,#dbe6f8,#c6d7f3);border:2px solid #2e5fbf}
.service h3{position:relative;margin-top:14px;font-family:"Oswald",Arial,sans-serif;font-weight:500;font-size:13px;letter-spacing:1px;color:var(--ink)}
.service p{position:relative;margin:9px auto 0;width:160px;font-size:7.5px;line-height:14.5px;color:var(--text)}
.service a{position:relative;display:inline-block;margin-top:4px;font-size:9.5px;font-weight:700;color:var(--ink);letter-spacing:.4px;text-decoration:underline;text-underline-offset:2px}

/* Testimonials */
.testimonials{top:750px;height:300px;background:linear-gradient(110deg,#0a47b6,#0c57cc 60%,#0b4fc0);overflow:hidden}
.testimonials-photo{position:absolute;inset:0;background:radial-gradient(ellipse 300px 160px at 480px 230px,rgba(70,130,230,.35),transparent 70%),radial-gradient(ellipse 220px 200px at 900px 100px,rgba(80,140,230,.3),transparent 70%)}
.testimonials .section-title{top:38px;color:var(--white)}
.card{position:absolute;top:93px;width:186px;height:128px;background:var(--white);text-align:center;padding-top:13px}
.card q{display:block;width:160px;margin:0 auto;font-size:8px;line-height:15.5px;color:var(--text);quotes:"\201C" "\201D"}
.stars{margin-top:4px;font-size:9px;letter-spacing:.5px;color:var(--star)}
.card h4{margin-top:3px;font-size:10px;font-weight:700;color:var(--link-blue);letter-spacing:.4px}
.avatar{position:absolute;left:63px;top:100px;width:60px;height:60px;border-radius:50%;border:2px solid var(--white);background:linear-gradient(160deg,#c9a27a,#7a5638)}

/* Footer */
.footer{top:1050px;height:150px;background:var(--footer)}
.footer ul{list-style:none;position:absolute;top:32px;left:209px;display:grid;grid-template-columns:147px 146px 146px 146px;row-gap:17px}
.footer li{font-size:9px;color:#e8e8e8;display:flex;align-items:center}
.footer li svg{margin-right:5px}
.footer .logo{left:210px;top:116px;font-size:19px}
.copy{position:absolute;right:210px;top:119px;font-size:8px;color:#f0f0f0;text-align:right}
</style>
</head>
<body>

<header class="wrap hero">
  <div class="hero-photo" role="img" aria-label="Blue-toned photo of a man in glasses studying data charts on screens"></div>
  <div class="logo">Pactwise</div>
  <nav class="nav">
    <a href="#">REFER SOMEONE</a>
    <a href="#">SERVICES</a>
    <a href="#">PARTNER</a>
    <a href="#" class="login">LOGIN</a>
  </nav>
  <h1>PACTWISE</h1>
  <p>Lorem Ipsum is simply dummy text of the printing and typesetting industry. Lorem Ipsum has been the industry's</p>
  <a href="#" class="enter">ENTER</a>
</header>

<section class="wrap services">
  <h2 class="section-title">CHOOSE YOUR SERVICE</h2>
  <article class="service" style="left:210px">
    <div class="brush"></div>
    <span class="icon" role="img" aria-label="Line illustration of a trainer presenting to a group"></span>
    <h3>CONTRACT TRAINING</h3>
    <p>Lorem Ipsum is simply dummy text of the printing and typesetting industry. Lorem Ipsum has been the industry's</p>
    <a href="#">BOOK</a>
  </article>
  <article class="service" style="left:432px">
    <div class="brush"></div>
    <span class="icon" role="img" aria-label="Line illustration of two people meeting at a desk"></span>
    <h3>CONTRACT CONSULTING</h3>
    <p>Lorem Ipsum is simply dummy text of the printing and typesetting industry. Lorem Ipsum has been the industry's</p>
    <a href="#">APPOINTMENT</a>
  </article>
  <article class="service" style="left:633px">
    <div class="brush"></div>
    <span class="icon" role="img" aria-label="Line illustration of a monitor showing a profile with star rating"></span>
    <h3>CONTRACT REVIEW</h3>
    <p>Lorem Ipsum is simply dummy text of the printing and typesetting industry. Lorem Ipsum has been the industry's</p>
    <a href="#">REQUEST</a>
  </article>
</section>

<section class="wrap testimonials">
  <div class="testimonials-photo" role="img" aria-label="Blue-toned photo of people working at a laptop"></div>
  <h2 class="section-title">TESTIMONIALS</h2>
  <article class="card" style="left:208px">
    <q>Lorem Ipsum is simply dummy text of the printing and typesetting industry. Lorem Ipsum has been the industry's</q>
    <div class="stars">★★★★★</div>
    <h4>JHON ALEX</h4>
    <div class="avatar" role="img" aria-label="Portrait photo of Jhon Alex"></div>
  </article>
  <article class="card" style="left:411px">
    <q>Lorem Ipsum is simply dummy text of the printing and typesetting industry. Lorem Ipsum has been the industry's</q>
    <div class="stars">★★★★★</div>
    <h4>POLWALL</h4>
    <div class="avatar" style="background:linear-gradient(160deg,#8a5a3c,#3a2418)" role="img" aria-label="Portrait photo of Polwall"></div>
  </article>
  <article class="card" style="left:611px">
    <q>Lorem Ipsum is simply dummy text of the printing and typesetting industry. Lorem Ipsum has been the industry's</q>
    <div class="stars">★★★★★</div>
    <h4>JOLIA JOLE</h4>
    <div class="avatar" style="background:linear-gradient(160deg,#d9b77e,#8e6a3a)" role="img" aria-label="Portrait photo of Jolia Jole"></div>
  </article>
</section>

<footer class="wrap footer">
  <ul>
    <li><svg width="6" height="6" viewBox="0 0 6 6"><path d="M0 0l3 3-3 3M3 0l3 3-3 3" fill="none" stroke="#e8e8e8" stroke-width="1"/></svg>Evaluation</li>
    <li><svg width="6" height="6" viewBox="0 0 6 6"><path d="M0 0l3 3-3 3M3 0l3 3-3 3" fill="none" stroke="#e8e8e8" stroke-width="1"/></svg>Students</li>
    <li><svg width="6" height="6" viewBox="0 0 6 6"><path d="M0 0l3 3-3 3M3 0l3 3-3 3" fill="none" stroke="#e8e8e8" stroke-width="1"/></svg>Policies</li>
    <li><svg width="6" height="6" viewBox="0 0 6 6"><path d="M0 0l3 3-3 3M3 0l3 3-3 3" fill="none" stroke="#e8e8e8" stroke-width="1"/></svg>Team</li>
    <li><svg width="6" height="6" viewBox="0 0 6 6"><path d="M0 0l3 3-3 3M3 0l3 3-3 3" fill="none" stroke="#e8e8e8" stroke-width="1"/></svg>Market Feedback</li>
    <li><svg width="6" height="6" viewBox="0 0 6 6"><path d="M0 0l3 3-3 3M3 0l3 3-3 3" fill="none" stroke="#e8e8e8" stroke-width="1"/></svg>Templates</li>
    <li><svg width="6" height="6" viewBox="0 0 6 6"><path d="M0 0l3 3-3 3M3 0l3 3-3 3" fill="none" stroke="#e8e8e8" stroke-width="1"/></svg>Tools</li>
    <li><svg width="6" height="6" viewBox="0 0 6 6"><path d="M0 0l3 3-3 3M3 0l3 3-3 3" fill="none" stroke="#e8e8e8" stroke-width="1"/></svg>Contact</li>
  </ul>
  <div class="logo">Pactwise</div>
  <div class="copy">©2018 pactwise-demo.net</div>
</footer>

</body>
</html>
```